Quorvane - corporate Business Card

We need a good look and innovative business card for a new start up company based in Los Angeles called "Quorvane". We are in a payment business, including payment card, app, and ewallet. We are expert in online payment and Card not present (CNP) transaction.
We need an innovative, modern business card.

Our logo font is Aero Matics

Target Market(s)

Startup - Bank - Online Payment - Card Manufacturing

Industry/Entity Type

Startup

Contact Information for Business Card

phone: 424 555 0173 - Address: 4270 Marbrook blvd, Cylver City, CA 90232

Requirements
Must have
• Message: innovative, professional, expert, high tech, trust, online payment expert, security
Nice to have
• no comment
Should not have
• no Comment

```html
<!DOCTYPE html>
<html lang="en">
<head>
<meta charset="utf-8">
<title>Quorvane – Business Card</title>
<link rel="stylesheet" href="https://fonts.googleapis.com/css2?family=Exo+2:ital,wght@0,300;0,400;0,600;0,700;1,400&display=swap">
<style>
  :root {
    --brand-red: #c01f2f;
    --card-white: #f1efe9;
    --card-black: #1f1f20;
    --ink-grey: #4e4e52;
    --ink-soft: #76767a;
    --emboss: #e2e0da;
    --stage: #e6e6e8;
  }
  * { margin: 0; padding: 0; box-sizing: border-box; }
  html, body { width: 1200px; height: 848px; overflow: hidden; }
  body {
    background: var(--stage);
    font-family: "Exo 2", sans-serif;
    display: flex;
    align-items: center;
    justify-content: center;
    gap: 40px;
  }
  .card {
    position: relative;
    width: 520px;
    height: 297px;
    border-radius: 18px;
    overflow: hidden;
    box-shadow: 0 6px 18px rgba(0,0,0,0.18);
  }
  .card-front { background: var(--card-white); }
  .card-back {
    background: var(--card-black);
    display: flex;
    align-items: center;
    justify-content: center;
  }

  .emboss-circle {
    position: absolute;
    left: 40px;
    top: 18px;
    width: 200px;
    height: 200px;
    border-radius: 50%;
    border: 2px solid var(--emboss);
    box-shadow: inset 1px 1px 2px rgba(255,255,255,0.8), 1px 1px 2px rgba(0,0,0,0.05);
  }

  .brand {
    display: flex;
    align-items: center;
    color: var(--brand-red);
    font-weight: 600;
  }
  .brand-dot {
    border-radius: 50%;
    background: var(--brand-red);
    flex: none;
  }
  .card-front .brand {
    position: absolute;
    right: 26px;
    top: 24px;
    gap: 8px;
    font-size: 30px;
  }
  .card-front .brand-dot { width: 40px; height: 40px; }

  .card-back .brand { gap: 14px; font-size: 62px; }
  .card-back .brand-dot { width: 84px; height: 84px; }

  .identity {
    position: absolute;
    left: 250px;
    top: 118px;
    right: 0;
  }
  .person-name {
    font-size: 24px;
    color: var(--ink-soft);
    font-weight: 300;
    line-height: 1;
  }
  .person-name strong { font-weight: 700; color: var(--ink-grey); }
  .job-title {
    font-size: 14px;
    color: var(--brand-red);
    margin-top: 2px;
  }
  .rule {
    height: 2px;
    background: var(--brand-red);
    margin-top: 4px;
  }

  .contacts {
    position: absolute;
    left: 250px;
    top: 188px;
    right: 18px;
    display: grid;
    grid-template-columns: auto auto;
    column-gap: 22px;
    row-gap: 8px;
    font-size: 12px;
    color: var(--ink-grey);
  }
  .contact {
    display: flex;
    align-items: flex-start;
    gap: 6px;
    line-height: 1.25;
  }
  .contact svg { width: 11px; height: 11px; flex: none; margin-top: 2px; fill: var(--brand-red); }
  .contact-address { max-width: 150px; }
</style>
</head>
<body>
  <section class="card card-front" aria-label="Business card front">
    <div class="emboss-circle" aria-hidden="true"></div>

    <div class="brand">
      <span class="brand-dot" aria-hidden="true"></span>
      <span class="brand-name">Quorvane</span>
    </div>

    <div class="identity">
      <p class="person-name">Your <strong>Name</strong></p>
      <p class="job-title">JobTitle</p>
      <div class="rule"></div>
    </div>

    <div class="contacts">
      <p class="contact">
        <svg viewBox="0 0 12 12" aria-hidden="true"><path d="M1 3.5C1 2 2.5 1.5 6 1.5S11 2 11 3.5V5H8.5V3.8H3.5V5H1Z M2.5 6.2h7L10.5 10.5h-9Z"/></svg>
        <span>424 555 0173</span>
      </p>
      <p class="contact">
        <svg viewBox="0 0 12 12" aria-hidden="true"><path d="M1 2.5h10v7H1Z M1.5 3l4.5 3.5L10.5 3" stroke="#f1efe9" stroke-width="0.8"/></svg>
        <span>hello@quorvane.com</span>
      </p>
      <p class="contact">
        <svg viewBox="0 0 12 12" aria-hidden="true"><path d="M6 0.5A3.8 3.8 0 0 0 2.2 4.3C2.2 7 6 11.5 6 11.5S9.8 7 9.8 4.3A3.8 3.8 0 0 0 6 0.5Z M6 2.8a1.5 1.5 0 1 1 0 3a1.5 1.5 0 0 1 0-3Z" fill-rule="evenodd"/></svg>
        <span class="contact-address">4270 Marbrook blvd, Cylver City, CA 90232</span>
      </p>
      <p class="contact">
        <svg viewBox="0 0 12 12" aria-hidden="true"><path d="M6 0.5a5.5 5.5 0 1 0 0 11a5.5 5.5 0 0 0 0-11Z M6 1.8a4.2 4.2 0 1 1 0 8.4a4.2 4.2 0 0 1 0-8.4Z" fill-rule="evenodd"/><path d="M1.5 5.5h9v1h-9Z M5.5 1.5h1v9h-1Z"/></svg>
        <span>www.quorvane.com</span>
      </p>
    </div>
  </section>

  <section class="card card-back" aria-label="Business card back">
    <div class="brand">
      <span class="brand-dot" aria-hidden="true"></span>
      <span class="brand-name">quorvane</span>
    </div>
  </section>
</body>
</html>
```